Bring Modern Tempo Business Card and logo

We need a logo design and business card for a new consulting firm called Bring Modern Tempo. We specialize in Digital Transformation of enterprises of all sizes. We help enterprises understand & significantly increase their business velocity. This requires changes in culture, organization, process and technology. We also partner with advanced technology companies to deliver tangible accelerated solutions. Methods utilized include Agile, Design Thinking, Advanced Technology Platforms (microservices, digital data, virtualization, blockchain, etc.). The final design should communicate velocity, transformation, growth and innovation.

Target Market(s)

Large Corporations and Enterprises

Contact Information for Business Card

Tagline - Charting Beyond Now

Logo Text

Bring Modern Tempo or an initial or initials or a symbol/picture

Requirements
Must have
• Front side: Logo, name of business (Bring Modern Tempo), tagline (Charting Beyond Now)
• Back side: First Name, Last Name, Title, Mobile Phone, Email, LinkedIn, URL (bringmoderntempo.com)
Nice to have
• The design should communicate velocity, transformation, growth and/or innovation.

```html
<!DOCTYPE html>
<html lang="en">
<head>
<meta charset="utf-8">
<title>Bring Modern Tempo – Business Card</title>
<link href="https://fonts.googleapis.com/css2?family=Questrial&family=Lato:wght@400;700&display=swap" rel="stylesheet">
<style>
  :root {
    --orange: #f97a26;
    --charcoal: #2d2d2d;
    --ink: #222222;
    --paper: #ffffff;
    --stage: #8a8a8a;
    --rule: #8c8c8c;
    --social: #1a7bc0;
  }
  * { box-sizing: border-box; margin: 0; padding: 0; }
  html, body { width: 1200px; height: 1200px; overflow: hidden; }
  body { background: var(--stage); position: relative; font-family: "Lato", sans-serif; }

  .card {
    position: absolute;
    top: 310px;
    width: 366px;
    height: 594px;
    overflow: hidden;
    box-shadow: 2px 3px 6px rgba(0,0,0,0.35);
  }
  .card--front { left: 233px; background: var(--paper); text-align: center; }
  .card--back { left: 628px; background: var(--charcoal); }

  /* Front */
  .brand-dot {
    position: absolute; left: 127px; top: 98px;
    width: 120px; height: 120px; border-radius: 50%;
    background: var(--orange);
  }
  .brand-name {
    position: absolute; left: 0; right: 0; top: 234px;
    font-family: "Questrial", sans-serif; font-size: 28px; color: var(--ink);
    letter-spacing: 0.2px;
  }
  .tagline {
    position: absolute; left: 0; right: 0; top: 270px;
    display: flex; align-items: center; justify-content: center; gap: 10px;
    font-family: "Questrial", sans-serif; font-size: 11px; letter-spacing: 2.4px;
    color: var(--orange); text-transform: uppercase; font-weight: 700;
  }
  .tagline::before, .tagline::after {
    content: ""; width: 42px; height: 1px; background: var(--orange);
  }
  .person-name {
    position: absolute; left: 0; right: 0; top: 372px;
    font-family: "Questrial", sans-serif; font-size: 24px; font-weight: 700;
    color: var(--orange); letter-spacing: 0.5px; text-transform: uppercase;
    -webkit-text-stroke: 0.4px var(--orange);
  }
  .person-title {
    position: absolute; left: 0; right: 0; top: 400px;
    font-size: 16px; color: var(--ink);
  }
  .contact-icons {
    position: absolute; left: 0; right: 0; top: 434px;
    display: flex; align-items: center; justify-content: center; gap: 3px;
  }
  .contact-icons .rule { width: 54px; height: 1px; background: var(--rule); margin: 0 4px; }
  .icon { width: 24px; height: 24px; display: block; }
  .contact-list {
    position: absolute; left: 0; right: 0; top: 470px;
    font-size: 16.5px; line-height: 22px; color: var(--ink);
  }

  /* Back */
  .back-band { position: absolute; left: 0; top: 0; width: 100%; height: 308px; background: var(--orange); }
  .back-ring { position: absolute; left: 0; top: 100px; }
  .back-name {
    position: absolute; left: 0; right: 0; top: 234px;
    text-align: center; font-family: "Questrial", sans-serif;
    font-size: 34px; line-height: 42px; color: var(--paper);
  }
  .social-row {
    position: absolute; left: 0; right: 0; top: 524px;
    display: flex; align-items: center; justify-content: center; gap: 6px;
  }
  .social-row .rule { width: 88px; height: 1px; background: #6a6a6a; }
  .social-dot { width: 28px; height: 28px; border-radius: 50%; background: var(--social); }
</style>
</head>
<body>

<section class="card card--front" aria-label="Card front">
  <div class="brand-dot"></div>
  <h1 class="brand-name">Bring Modern Tempo</h1>
  <p class="tagline">Charting Beyond Now</p>

  <h2 class="person-name">Daniel Hartley</h2>
  <p class="person-title">Managing Director</p>

  <div class="contact-icons">
    <span class="rule"></span>
    <svg class="icon" viewBox="0 0 24 24" aria-label="Phone">
      <circle cx="12" cy="12" r="12" fill="#f97a26"/>
      <path d="M7 9.5c0-1 .8-1.8 1.8-1.8h6.4c1 0 1.8.8 1.8 1.8v.8h-2.2v-1h-5.6v1H7z M8.5 11.5h7l1 4.5h-9z" fill="#fff"/>
      <circle cx="12" cy="13.6" r="1.3" fill="#f97a26"/>
    </svg>
    <svg class="icon" viewBox="0 0 24 24" aria-label="Email">
      <circle cx="12" cy="12" r="12" fill="#f97a26"/>
      <rect x="6.5" y="8" width="11" height="8" rx="1" fill="#fff"/>
      <path d="M6.8 8.4 12 12.6l5.2-4.2" fill="none" stroke="#f97a26" stroke-width="1.2"/>
    </svg>
    <svg class="icon" viewBox="0 0 24 24" aria-label="Website">
      <circle cx="12" cy="12" r="12" fill="#f97a26"/>
      <circle cx="12" cy="12" r="6" fill="none" stroke="#fff" stroke-width="1.5"/>
      <path d="M10 8.5c1.5.5 1 2 2.5 2.5s1 2 0 3" fill="none" stroke="#fff" stroke-width="1.5"/>
    </svg>
    <span class="rule"></span>
  </div>

  <address class="contact-list" style="font-style:normal">
    044-987 654 321<br>
    hello@bringmoderntempo.com<br>
    www.bringmoderntempo.com
  </address>
</section>

<section class="card card--back" aria-label="Card back">
  <div class="back-band"></div>
  <svg class="back-ring" width="366" height="380" viewBox="0 0 366 380" aria-hidden="true">
    <circle cx="183" cy="188" r="172" fill="none" stroke="#ffffff" stroke-width="26"/>
  </svg>
  <p class="back-name">Bring Modern<br>Tempo</p>
  <div class="social-row">
    <span class="rule"></span>
    <span class="social-dot" aria-label="Professional network profile"></span>
    <span class="rule"></span>
  </div>
</section>

</body>
</html>
```